Dental Office Needs Exciting New Stationary

We need a stationary design that incorporates the logo that we already have and would like to keep the existing color scheme. We need something clean and professional. This is a Endodontic (root canals) office and must represent a dental specialist's office. I need a design for a business card, envelope, and letterhead that all coordinate. I would like the business card to incorporate the information in the business card sample that I am providing. I made the business card design myself but would like to see a better one.

```html
<!DOCTYPE html>
<html lang="en">
<head>
<meta charset="utf-8">
<title>Summit Endodontics Stationery</title>
<link href="https://fonts.googleapis.com/css2?family=Montserrat:wght@600&family=Arimo:wght@400;700&display=swap" rel="stylesheet">
<style>
  :root {
    --bg: #3a3a3c;
    --paper: #ffffff;
    --brand-blue: #1f74c4;
    --accent-gray: #b4b6b9;
    --accent-purple: #8a8cbd;
    --ink-navy: #1e2a6e;
    --ink-dark: #2a2a2a;
    --pale-blue: #c7dcf2;
  }
  * { margin: 0; padding: 0; box-sizing: border-box; }
  html, body { width: 1200px; height: 1022px; overflow: hidden; }
  body { background: var(--bg); position: relative; font-family: "Arimo", Arial, sans-serif; }

  .piece { position: absolute; background: var(--paper); overflow: hidden; }

  .letterhead { left: 46px; top: 50px; width: 678px; height: 902px; }
  .envelope { left: 377px; top: 235px; width: 775px; height: 343px; }
  .card-front { left: 767px; top: 588px; width: 299px; height: 173px; }
  .card-back { left: 852px; top: 780px; width: 300px; height: 172px; }

  .header-tone { position: absolute; left: 0; top: 0; right: 0;
    background: linear-gradient(90deg, var(--paper) 45%, var(--accent-purple) 100%); }
  .letterhead .header-tone { height: 140px; }
  .envelope .header-tone { height: 120px; }
  .footer-band { position: absolute; left: 0; right: 0; bottom: 0; background: var(--accent-gray); }
  .letterhead .footer-band { height: 16px; }
  .envelope .footer-band { height: 8px; }
  .card-front .base-tone { position: absolute; left: 0; right: 0; bottom: 0; height: 52px;
    background: linear-gradient(180deg, #e1ecf8, var(--pale-blue)); }
  .card-back .rule { position: absolute; left: 0; right: 0; top: 68px; height: 3px; background: var(--accent-gray); }

  .brand { position: absolute; display: flex; align-items: center; gap: 14px; }
  .brand-dot { border-radius: 50%; background: var(--brand-blue); flex: none; }
  .brand-name { font-family: "Montserrat", Arial, sans-serif; font-weight: 600; color: var(--brand-blue); line-height: 1; }
  .brand-name span { display: block; }
  .brand-name .sub { letter-spacing: 0.18em; margin-top: 4px; }

  .letterhead .brand { left: 40px; top: 34px; }
  .letterhead .brand-dot { width: 56px; height: 56px; }
  .letterhead .brand-name .main { font-size: 40px; }
  .letterhead .brand-name .sub { font-size: 17px; }

  .envelope .brand { left: 49px; top: 31px; }
  .envelope .brand-dot { width: 56px; height: 56px; }
  .envelope .brand-name .main { font-size: 40px; }
  .envelope .brand-name .sub { font-size: 17px; }

  .card-front .brand { left: 38px; top: 42px; gap: 10px; }
  .card-front .brand-dot { width: 40px; height: 40px; }
  .card-front .brand-name .main { font-size: 29px; }
  .card-front .brand-name .sub { font-size: 12px; }

  .card-back .brand { left: 64px; top: 12px; gap: 9px; }
  .card-back .brand-dot { width: 32px; height: 32px; }
  .card-back .brand-name .main { font-size: 22px; }
  .card-back .brand-name .sub { font-size: 9.5px; margin-top: 3px; }

  .address { position: absolute; font-size: 8px; line-height: 1.25; color: var(--ink-navy); text-transform: uppercase; white-space: nowrap; }
  .web { position: absolute; font-size: 8px; color: var(--ink-navy); text-transform: uppercase; }

  .envelope .office-a { left: 71px; top: 204px; }
  .envelope .office-b { left: 215px; top: 204px; }
  .envelope .web { left: 166px; top: 241px; }
  .envelope .window { position: absolute; left: 419px; top: 184px; width: 281px; height: 102px; border: 1px solid #b9bbbe; border-radius: 14px; }

  .card-back .doctors { position: absolute; left: 0; right: 0; top: 80px; text-align: center; font-size: 11px; letter-spacing: 0.08em; line-height: 1.35; color: var(--ink-dark); }
  .card-back .address { font-size: 6.6px; font-weight: 700; top: 122px; }
  .card-back .office-a { left: 28px; }
  .card-back .office-b { left: 162px; }
  .card-back .web { left: 0; right: 0; top: 155px; text-align: center; font-size: 6.6px; font-weight: 700; }
</style>
</head>
<body>

<section class="piece letterhead" aria-label="Letterhead">
  <div class="header-tone" role="img" aria-label="Decorative header graphic in blue, gray and purple"></div>
  <div class="brand">
    <div class="brand-dot"></div>
    <div class="brand-name"><span class="main">SUMMIT</span><span class="sub">ENDODONTICS</span></div>
  </div>
  <div class="footer-band" role="img" aria-label="Decorative footer graphic"></div>
</section>

<section class="piece envelope" aria-label="Envelope">
  <div class="header-tone" role="img" aria-label="Decorative header graphic in blue, gray and purple"></div>
  <div class="brand">
    <div class="brand-dot"></div>
    <div class="brand-name"><span class="main">SUMMIT</span><span class="sub">ENDODONTICS</span></div>
  </div>
  <p class="address office-a">1480 Elm Street<br>Riverton, CA 95800<br>O&nbsp; 555.201.3400 &nbsp; F&nbsp; 555.201.3401</p>
  <p class="address office-b">4200 Oak Ave. Suite #2<br>Fairview, CA 95600<br>O&nbsp; 555.310.2200 &nbsp; F&nbsp; 555.310.2201</p>
  <p class="web">summitendo.com</p>
  <div class="window"></div>
  <div class="footer-band" role="img" aria-label="Decorative footer graphic"></div>
</section>

<section class="piece card-front" aria-label="Business card front">
  <div class="base-tone" role="img" aria-label="Decorative pale blue base graphic"></div>
  <div class="brand">
    <div class="brand-dot"></div>
    <div class="brand-name"><span class="main">SUMMIT</span><span class="sub">ENDODONTICS</span></div>
  </div>
</section>

<section class="piece card-back" aria-label="Business card back">
  <div class="brand">
    <div class="brand-dot"></div>
    <div class="brand-name"><span class="main">SUMMIT</span><span class="sub">ENDODONTICS</span></div>
  </div>
  <div class="rule"></div>
  <p class="doctors">DANIEL R MERCER DDS MS<br>MARCO L ALVAREZ DDS</p>
  <p class="address office-a">1480 Elm Street<br>Riverton, CA 95800<br>O&nbsp; 555.201.3400 &nbsp; F&nbsp; 555.201.3401</p>
  <p class="address office-b">4200 Oak Ave. Suite #2<br>Fairview, CA 95600<br>O&nbsp; 555.310.2200 &nbsp; F&nbsp; 555.310.2201</p>
  <p class="web">summitendo.com</p>
</section>

</body>
</html>
```